Womans Supplement Designs

Launching a Supplement company and need to get some initial designs created, I've attached our logo and the bottle type that I want the samples done one.

This project is for our Whey Protein we are starting with Vanilla, chocolate and strawberry banana

(ALL DESIGN VARIATIONS MUST BE A WHITE BOTTLE NOT BLACK)

(FOR DESIGN SAMPLES PLEASE USE THE SUPPLEMENT BOTTLE STYLE I PROVIDED)

Whoever is selected the winner I will have more work for you to complete the disigns for the rest of the products in the line, Just want to get this shake completed first

Target Market(s)

Women

Requirements
Must have
• Must have our current logo involved

the name of this product will be "KIVA LUM"

Must have this slogan,

ALL-IN-ONE PREMIUM PROTEIN NUTRITIONAL SHAKE FOR BLACK WOMEN

This is our meal replacement

the design should try to keep the same look and feel of the existing provided supplement images

we are starting with chocolate, vanilla and strawberry banana

this is for women and should look colorful and appeal to them
Should not have
• Do not use an image of a person or lady, don't want it branded to a person

```html
<!DOCTYPE html>
<html lang="en">
<head>
<meta charset="UTF-8">
<title>Kiva Lum Protein Labels</title>
<link rel="stylesheet" href="https://fonts.googleapis.com/css2?family=Montserrat:wght@400;500;600;800&display=swap">
<style>
  :root {
    --page: #efefef;
    --label: #ffffff;
    --ink: #2e2e2e;
    --ink-soft: #3d3d3d;
    --band-light: #93d1b4;
    --band-dark: #5ea383;
    --strip-light: #c2e4d5;
    --strip-dark: #92b8a6;
    --vanilla: #93bcc6;
    --chocolate: #c6a48c;
  }
  * { box-sizing: border-box; margin: 0; padding: 0; }
  html, body {
    width: 1200px; height: 800px; overflow: hidden;
    background: var(--page);
    font-family: "Montserrat", sans-serif;
    color: var(--ink);
  }
  .lineup {
    position: relative; width: 1200px; height: 800px;
  }
  .label {
    position: absolute; top: 250px;
    width: 326px; height: 410px;
    background: var(--label);
    border-radius: 28px;
    overflow: hidden;
    display: flex; flex-direction: column; align-items: center;
  }
  .label--vanilla { left: 217px; }
  .label--chocolate { left: 644px; }

  .brand {
    height: 142px;
    display: flex; flex-direction: column; align-items: center; justify-content: flex-end;
    padding-bottom: 18px;
  }
  .brand-mark {
    width: 14px; height: 14px; background: var(--ink); margin-bottom: 12px;
  }
  .brand-name {
    font-size: 12px; font-weight: 600; letter-spacing: 1.5px;
  }
  .brand-line {
    font-size: 6px; font-weight: 600; letter-spacing: 4px; margin-top: 6px;
  }
  .brand-sub {
    font-size: 4px; font-weight: 600; letter-spacing: 1px; margin-top: 5px;
  }

  .hero-band {
    width: 100%; height: 131px;
    background: linear-gradient(90deg, var(--band-light) 0%, var(--band-light) 25%, var(--band-dark) 90%);
    text-align: center; padding-top: 14px;
  }
  .product-name {
    font-size: 32px; font-weight: 800; line-height: 1; letter-spacing: 0.5px;
  }
  .tagline {
    font-size: 20px; font-weight: 600; line-height: 1.22; color: var(--ink-soft);
    margin-top: 6px; letter-spacing: 0.3px;
  }
  .slogan {
    font-size: 9px; font-weight: 400; color: var(--ink-soft); margin-top: 2px; letter-spacing: 0.2px;
  }

  .claims-strip {
    width: 100%; height: 58px;
    background: linear-gradient(90deg, var(--strip-light) 0%, var(--strip-light) 30%, var(--strip-dark) 100%);
    display: flex; justify-content: center; align-items: center;
  }
  .claim {
    font-size: 11px; font-weight: 500; line-height: 1.1; text-align: center;
    padding: 0 10px;
  }
  .claim + .claim { border-left: 1.5px solid var(--ink); }

  .flavour {
    margin-top: 6px;
    width: 114px; height: 20px; border-radius: 4px;
    font-size: 12px; font-weight: 500; letter-spacing: 0.5px;
    display: flex; align-items: center; justify-content: center;
  }
  .flavour--vanilla { background: var(--vanilla); }
  .flavour--chocolate { background: var(--chocolate); }

  .net-weight {
    margin-top: 29px; font-size: 10px; font-weight: 600;
  }
</style>
</head>
<body>
<main class="lineup">
  <section class="label label--vanilla">
    <header class="brand">
      <span class="brand-mark"></span>
      <span class="brand-name">NOVA HER</span>
      <span class="brand-line">LIFESTYLE</span>
      <span class="brand-sub">NUTRITION</span>
    </header>
    <div class="hero-band">
      <h1 class="product-name">KIVA LUM</h1>
      <p class="tagline">ALL-IN-ONE<br>PREMIUM PROTEIN</p>
      <p class="slogan">NUTRITIONAL SHAKE FOR BLACK WOMEN</p>
    </div>
    <div class="claims-strip">
      <span class="claim">100<br>cals</span>
      <span class="claim">low<br>sugar</span>
      <span class="claim">gluten<br>free</span>
    </div>
    <div class="flavour flavour--vanilla">VANILLA</div>
    <p class="net-weight">NET 1KGS</p>
  </section>

  <section class="label label--chocolate">
    <header class="brand">
      <span class="brand-mark"></span>
      <span class="brand-name">NOVA HER</span>
      <span class="brand-line">LIFESTYLE</span>
      <span class="brand-sub">NUTRITION</span>
    </header>
    <div class="hero-band">
      <h1 class="product-name">KIVA LUM</h1>
      <p class="tagline">ALL-IN-ONE<br>PREMIUM PROTEIN</p>
      <p class="slogan">NUTRITIONAL SHAKE FOR BLACK WOMEN</p>
    </div>
    <div class="claims-strip">
      <span class="claim">100<br>cals</span>
      <span class="claim">low<br>sugar</span>
      <span class="claim">gluten<br>free</span>
    </div>
    <div class="flavour flavour--chocolate">CHOCOLATE</div>
    <p class="net-weight">NET 1KGS</p>
  </section>
</main>
</body>
</html>
```